Scrap Metal Recycling

We are looking for a simple yet bold business card. We already have the logo, please see attached. Color scheme of blue, black and white or just blue and white.

```html
<!DOCTYPE html>
<html lang="en">
<head>
<meta charset="utf-8">
<title>Ridgeline Metals Inc. – Business Card</title>
<link rel="stylesheet" href="https://fonts.googleapis.com/css2?family=Montserrat:wght@400;500;700&display=swap">
<style>
  :root {
    --bg: #e4e4e4;
    --card-white: #ffffff;
    --brand-blue: #1a8fb5;
    --ink: #333333;
    --ink-soft: #4a4a4a;
    --rule: #6e6e6e;
    --back-dark: #2f2f30;
    --back-dark-2: #3a3a3b;
  }
  * { box-sizing: border-box; margin: 0; padding: 0; }
  html, body {
    width: 1200px; height: 801px; overflow: hidden;
    background: var(--bg);
    font-family: "Montserrat", Arial, sans-serif;
  }
  .stage {
    position: relative; width: 1200px; height: 801px;
    display: flex; align-items: center; justify-content: center; gap: 40px;
  }
  .card {
    position: relative; width: 540px; height: 309px;
    box-shadow: 0 6px 18px rgba(0,0,0,0.18);
    overflow: hidden;
  }
  /* Front */
  .card-front { background: var(--card-white); }
  .card-front .accent-band {
    position: absolute; left: 0; right: 0; bottom: 0; height: 11px;
    background: var(--brand-blue);
  }
  .brand {
    position: absolute; top: 48px; left: 190px; width: 310px; text-align: center;
  }
  .brand-name {
    font-weight: 700; font-size: 27px; color: var(--ink);
    letter-spacing: 0.5px; text-transform: uppercase;
  }
  .brand-tagline {
    margin-top: 6px; font-weight: 500; font-size: 13px; color: var(--brand-blue);
    letter-spacing: 4px; text-transform: uppercase;
  }
  .person {
    position: absolute; left: 38px; top: 164px;
  }
  .person-name {
    font-weight: 700; font-size: 21px; color: var(--brand-blue); letter-spacing: 0.5px;
  }
  .person-role { font-size: 14px; color: var(--ink-soft); margin-top: 1px; }
  .divider {
    position: absolute; left: 38px; right: 32px; top: 218px; height: 1px;
    background: var(--rule);
  }
  .address {
    position: absolute; right: 32px; top: 170px; text-align: right;
    font-size: 13px; line-height: 1.35; color: var(--ink-soft);
  }
  .contact {
    position: absolute; left: 38px; top: 226px; list-style: none;
    font-size: 13px; line-height: 19px; color: var(--ink-soft);
  }
  .contact li { display: flex; align-items: center; gap: 7px; }
  .contact svg { width: 12px; height: 12px; flex: none; }
  /* Back */
  .card-back {
    background: linear-gradient(135deg, var(--back-dark-2), var(--back-dark));
  }
  .back-texture { position: absolute; inset: 0; }
  .back-brand {
    position: absolute; right: 40px; bottom: 70px; text-align: center;
  }
  .back-brand .brand-name { color: #ffffff; font-size: 22px; }
  .back-brand .brand-tagline { color: #ffffff; font-size: 10px; letter-spacing: 3px; }
</style>
</head>
<body>
<main class="stage">
  <section class="card card-front" aria-label="Business card front">
    <div class="brand">
      <div class="brand-name">Ridgeline Metals Inc.</div>
      <div class="brand-tagline">Scrap Metal Recycling</div>
    </div>
    <div class="person">
      <div class="person-name">JONATHAN SMITH</div>
      <div class="person-role">Manager</div>
    </div>
    <div class="address">Your address, city<br>state, ZIP 0000</div>
    <div class="divider"></div>
    <ul class="contact">
      <li>
        <svg viewBox="0 0 12 12"><circle cx="6" cy="6" r="6" fill="var(--brand-blue)"/><path d="M4 3.2c.5 2.4 2 4 4.6 4.8l.4-1-1.2-.6-.6.6c-.8-.4-1.4-1-1.8-1.8l.6-.6L5.4 3.4z" fill="#fff"/></svg>
        123-456-2100
      </li>
      <li>
        <svg viewBox="0 0 12 12"><circle cx="6" cy="6" r="6" fill="var(--brand-blue)"/><rect x="3" y="4" width="6" height="4.2" fill="#fff"/><path d="M3 4l3 2.3L9 4" stroke="var(--brand-blue)" stroke-width="0.7" fill="none"/></svg>
        youremail@mailbox.com
      </li>
      <li>
        <svg viewBox="0 0 12 12"><circle cx="6" cy="6" r="6" fill="var(--brand-blue)"/><circle cx="6" cy="6" r="3.2" stroke="#fff" stroke-width="0.8" fill="none"/><path d="M2.8 6h6.4M6 2.8v6.4" stroke="#fff" stroke-width="0.7"/></svg>
        www.yourwebsite.com
      </li>
    </ul>
    <div class="accent-band"></div>
  </section>

  <section class="card card-back" aria-label="Business card back">
    <div class="back-texture" role="img" aria-label="Embossed tone-on-tone repeating brand pattern across the dark card back"></div>
    <div class="back-brand">
      <div class="brand-name">Ridgeline Metals Inc.</div>
      <div class="brand-tagline">Scrap Metal Recycling</div>
    </div>
  </section>
</main>
</body>
</html>
```